Business Card Design

We like to use greens as you will see in our logo (but not TOO much green). We are a Dental Clinic in a somewhat eccentric community. We do not like the dated sharp designs which we see many dentists use. We're looking for something bright and fresh while still maintaining the integrity of the profession. Elegance is not necessarily what we are going for... we need for the design to be "mature" but also up-lifting.

See our logo.
Updates

Project Deadline Extended
Reason: We have 5 designs which we like. But we'd like to see a few more before committing to a design.

Project Deadline Extended
Reason: We are awaiting revisions to this project. We are still welcoming designs while we wait to see if designers are able to provide to us the revisions we require in order to proceed with a selection.

Target Market(s)

Younger families - ages late 20's to early 40's

Industry/Entity Type

Business

Contact Information for Business Card

Marlow T. Benning DDS 2740 W. Hollister Rd. Ste. 7 Royal Oak, MI 48133 (248)555-0193 FX (248)555-0147 info@BrightwellDentalCareMi.example BrigthwellDentalCareMi.example on the back of the card we need an appointment reminder (For____ Date___ Time____) with "If you are unable to keep your appointment, kindly give 48 hours notice" at the bottom. No use of teeth in the design. DOUBLE SIDED DESIGN

Requirements
Should not have
• The use of pictures of teeth

```html
<!DOCTYPE html>
<html lang="en">
<head>
<meta charset="utf-8">
<title>Brightwell Dental Care – Business Card</title>
<link rel="stylesheet" href="https://fonts.googleapis.com/css2?family=Oswald:wght@400;500&family=Josefin+Sans:wght@600&display=swap">
<style>
  :root {
    --stage: #e9e9e7;
    --card: #c7d692;
    --band: #8cbd4b;
    --ink: #2d6a3b;
    --band-ink: #f4f8ea;
    --soft-circle: #b3cb7e;
  }
  * { box-sizing: border-box; margin: 0; padding: 0; }
  html, body { width: 1200px; height: 900px; overflow: hidden; }
  body {
    background: var(--stage);
    position: relative;
    font-family: "Oswald", "Arial Narrow", sans-serif;
  }
  .card {
    position: absolute;
    left: 365px;
    width: 553px;
    height: 355px;
    background: var(--card);
    border-radius: 22px;
    overflow: hidden;
  }
  .card--back { top: 30px; }
  .card--front { top: 400px; }

  .band-block {
    position: absolute;
    left: 0; top: 235px;
    width: 45px; height: 92px;
    background: var(--band);
  }
  .band-panel {
    position: absolute;
    left: 232px; top: 235px;
    width: 321px; height: 92px;
    background: var(--band);
    color: var(--band-ink);
  }

  /* back side */
  .accent-circle {
    position: absolute;
    left: 360px; top: 35px;
    width: 190px; height: 190px;
    border-radius: 50%;
    background: var(--soft-circle);
    opacity: .75;
  }
  .appointment-field {
    position: absolute;
    left: 50px;
    display: flex;
    align-items: flex-end;
    color: var(--ink);
    font-weight: 500;
    font-size: 14px;
    letter-spacing: .3px;
  }
  .appointment-field .label { width: 37px; }
  .appointment-field .colon { width: 8px; }
  .appointment-field .blank {
    width: 263px;
    border-bottom: 2px solid var(--ink);
    margin-bottom: 4px;
  }
  .field-for { top: 74px; }
  .field-date { top: 114px; }
  .field-time { top: 154px; }

  .brand-name {
    color: var(--ink);
    font-family: "Josefin Sans", sans-serif;
    font-weight: 600;
    text-align: center;
    line-height: 1.05;
  }
  .card--back .brand-name {
    position: absolute;
    left: 45px; top: 246px;
    width: 187px;
    font-size: 25px;
  }
  .cancel-notice {
    display: flex;
    flex-direction: column;
    justify-content: space-around;
    height: 100%;
    padding: 12px 0;
    text-align: center;
    font-size: 13px;
    font-weight: 400;
    text-transform: uppercase;
  }

  /* front side */
  .card--front .brand-name {
    position: absolute;
    left: 0; top: 70px;
    width: 100%;
    font-size: 46px;
  }
  .address {
    position: absolute;
    left: 0; top: 202px;
    width: 100%;
    text-align: center;
    color: var(--ink);
    font-size: 15px;
    font-weight: 500;
    text-transform: uppercase;
  }
  .dentist-name {
    position: absolute;
    left: 52px; top: 268px;
    color: var(--ink);
    font-size: 22px;
    font-weight: 500;
    text-transform: uppercase;
  }
  .contact-list {
    list-style: none;
    padding: 2px 0 0 12px;
  }
  .contact-list li {
    display: flex;
    align-items: center;
    height: 23px;
    font-size: 13.5px;
    text-transform: uppercase;
  }
  .contact-list svg { width: 13px; height: 13px; margin-right: 6px; flex: none; }
</style>
</head>
<body>

<section class="card card--back" aria-label="Appointment reminder side">
  <div class="accent-circle"></div>
  <div class="appointment-field field-for"><span class="label">FOR</span><span class="colon">:</span><span class="blank"></span></div>
  <div class="appointment-field field-date"><span class="label">DATE</span><span class="colon">:</span><span class="blank"></span></div>
  <div class="appointment-field field-time"><span class="label">TIME</span><span class="colon">:</span><span class="blank"></span></div>
  <div class="band-block"></div>
  <div class="brand-name">Brightwell<br>Dental Care</div>
  <div class="band-panel">
    <p class="cancel-notice">
      <span>"If you are unable to keep your appointment,</span>
      <span>kindly give 48 hours notice"</span>
    </p>
  </div>
</section>

<section class="card card--front" aria-label="Contact side">
  <div class="brand-name">Brightwell<br>Dental Care</div>
  <p class="address">2740 W. Hollister Rd. Ste. 7 Royal Oak, MI 48133</p>
  <div class="band-block"></div>
  <p class="dentist-name">Marlow T. Benning DDS</p>
  <div class="band-panel">
    <ul class="contact-list">
      <li><svg viewBox="0 0 14 14"><circle cx="7" cy="7" r="7" fill="#c9dba4"/><path d="M4.5 3.5l1.5 0 .6 2-1 .8a5 5 0 0 0 2.1 2.1l.8-1 2 .6v1.5c0 .6-.5 1-1.1 1A6.5 6.5 0 0 1 3.5 4.6c0-.6.4-1.1 1-1.1z" fill="#8cbd4b"/></svg>(248)555-0193</li>
      <li><svg viewBox="0 0 14 14"><circle cx="7" cy="7" r="7" fill="#c9dba4"/><rect x="4.5" y="3" width="5" height="3" fill="#8cbd4b"/><rect x="3" y="6" width="8" height="3.5" rx=".6" fill="#8cbd4b"/><rect x="4.5" y="9" width="5" height="2.2" fill="#8cbd4b"/></svg>(248)555-0147</li>
      <li><svg viewBox="0 0 14 14"><circle cx="7" cy="7" r="7" fill="#c9dba4"/><rect x="3" y="4.2" width="8" height="5.6" rx=".6" fill="#8cbd4b"/><path d="M3.3 4.6L7 7.4l3.7-2.8" stroke="#c9dba4" stroke-width=".9" fill="none"/></svg>info@BrightwellDentalCareMi.example</li>
      <li><svg viewBox="0 0 14 14"><circle cx="7" cy="7" r="7" fill="#c9dba4"/><circle cx="7.6" cy="6.2" r="2.4" stroke="#8cbd4b" stroke-width="1.3" fill="none"/><path d="M5.9 7.9L3.8 10" stroke="#8cbd4b" stroke-width="1.5"/></svg>www.BrigthwellDentalCareMi.example</li>
    </ul>
  </div>
</section>

</body>
</html>
```